New Business Card Design Project - Moreland Bookkeeping & Tax Services, LLC

Below is a sample image of the card (Fenwick Ledger). I would like to have a designed business card that looks very similar (Front & Back). In addition, I would like to keep the same colors as well. I attached my Business Logo (Moreland Bookkeeping & Tax Services, LLC) that will be on my website.

Target Market(s)

Executives, Business Owners, Board of Directors, Chief Financial Officers

Contact Information for Business Card

Font styles to use
Serif

Colors
0c5ba6
ffffff
5c5c5c

Requirements
Must have
• My Name: Calvin Prewitt, CPA
• Position: Owner
• Phone: (555) 555-0148
• Email: Cprewitt@morelandbooks.com
• Website: www.Morelandbooks.com
• Address: 42917 Birch Hollow Dr #2306
• Ashgrove Falls, LN 21190
Nice to have
• Same design & color scheme as Fenwick Ledgr Business card sample attached

```html
<!DOCTYPE html>
<html lang="en">
<head>
<meta charset="utf-8">
<title>Moreland Bookkeeping &amp; Tax Services – Business Card</title>
<link rel="stylesheet" href="https://fonts.googleapis.com/css2?family=Libre+Baskerville&family=Arimo:wght@400;700&display=swap">
<style>
  :root {
    --brand-blue: #0c5ba6;
    --brand-white: #ffffff;
    --brand-grey: #5c5c5c;
    --ink: #1c1c1c;
    --rule: #3a3a3a;
    --stage: #2b2b2b;
    --paper-shade: #ececec;
  }
  * { box-sizing: border-box; margin: 0; padding: 0; }
  html, body { width: 1200px; height: 997px; overflow: hidden; }
  body {
    background: var(--stage);
    font-family: "Arimo", Arial, sans-serif;
    position: relative;
  }
  .card {
    position: absolute;
    width: 540px;
    height: 309px;
    top: 344px;
    overflow: hidden;
    box-shadow: 0 18px 40px rgba(0,0,0,.55);
  }
  /* ---------- Back ---------- */
  .card-back { left: 30px; background: var(--brand-blue); }
  .card-back .company-name {
    position: absolute;
    right: 26px;
    top: 146px;
    white-space: nowrap;
    font-family: "Libre Baskerville", Georgia, serif;
    font-size: 13px;
    letter-spacing: 1.4px;
    text-transform: uppercase;
    color: var(--brand-white);
  }
  /* ---------- Front ---------- */
  .card-front {
    left: 630px;
    background: linear-gradient(160deg, var(--brand-white) 0%, var(--paper-shade) 100%);
  }
  .brand-lockup {
    position: absolute;
    left: 34px;
    top: 56px;
    display: flex;
    align-items: center;
    gap: 10px;
    white-space: nowrap;
  }
  .brand-mark { width: 14px; height: 14px; background: var(--brand-blue); }
  .brand-lockup .company-name {
    font-family: "Libre Baskerville", Georgia, serif;
    font-size: 14.5px;
    letter-spacing: 1.4px;
    text-transform: uppercase;
    color: var(--brand-blue);
  }
  .rule { position: absolute; height: 1px; background: var(--rule); }
  .rule-brand { left: 58px; right: 26px; top: 84px; }
  .rule-name { left: 210px; right: 26px; top: 150px; }
  .person { position: absolute; left: 34px; top: 132px; white-space: nowrap; }
  .person-name { font-size: 17px; color: var(--brand-blue); }
  .person-title { font-size: 11px; color: var(--ink); margin-top: 3px; }
  .contact-list {
    position: absolute;
    left: 34px;
    top: 208px;
    list-style: none;
    font-size: 12.5px;
    color: var(--ink);
    white-space: nowrap;
  }
  .contact-list li { display: flex; align-items: center; gap: 9px; height: 20px; }
  .contact-icon { width: 13px; height: 13px; }
  .address {
    position: absolute;
    right: 24px;
    top: 186px;
    text-align: right;
    font-size: 11px;
    line-height: 16px;
    color: var(--ink);
    white-space: nowrap;
  }
  .band { position: absolute; }
  .band-web {
    right: 0; top: 224px; width: 196px; height: 34px;
    background: var(--brand-blue);
    clip-path: polygon(6% 0, 100% 0, 100% 100%, 0 100%);
    color: var(--brand-white);
    font-size: 12px; font-weight: 700;
    letter-spacing: .3px;
    display: flex; align-items: center; justify-content: center;
  }
  .band-grey {
    left: 0; bottom: 0; width: 372px; height: 48px;
    background: var(--brand-grey);
    clip-path: polygon(0 0, 100% 0, 96% 100%, 0 100%);
  }
  .band-base { left: 0; right: 0; bottom: 0; height: 8px; background: var(--brand-grey); }
</style>
</head>
<body>

  <section class="card card-back" aria-label="Card back">
    <p class="company-name">Moreland Bookkeeping &amp; Tax Services</p>
  </section>

  <section class="card card-front" aria-label="Card front">
    <div class="brand-lockup">
      <span class="brand-mark"></span>
      <span class="company-name">Moreland Bookkeeping &amp; Tax Services</span>
    </div>
    <div class="rule rule-brand"></div>

    <div class="person">
      <p class="person-name">Calvin Prewitt, CPA</p>
      <p class="person-title">Owner</p>
    </div>
    <div class="rule rule-name"></div>

    <ul class="contact-list">
      <li>
        <svg class="contact-icon" viewBox="0 0 16 16" aria-hidden="true">
          <circle cx="8" cy="8" r="8" fill="#0c5ba6"/>
          <path d="M4 6.2c0-1 .8-1.6 4-1.6s4 .6 4 1.6l-1.4.6-.6-1H6l-.6 1zM5.4 7.4h5.2l.9 3.6H4.5z" fill="#fff"/>
        </svg>
        (555) 555-0148
      </li>
      <li>
        <svg class="contact-icon" viewBox="0 0 16 16" aria-hidden="true">
          <circle cx="8" cy="8" r="8" fill="#0c5ba6"/>
          <rect x="5.5" y="3.5" width="5" height="9" rx="1" fill="none" stroke="#fff" stroke-width="1.2"/>
        </svg>
        Cprewitt@morelandbooks.com
      </li>
    </ul>

    <p class="address">42917 Birch Hollow Dr #2306<br>Ashgrove Falls, LN 21190</p>

    <div class="band band-web">www.morelandbooks.com</div>
    <div class="band band-grey"></div>
    <div class="band band-base"></div>
  </section>

</body>
</html>
```